Style sheet & templates for a people friendly AI services company

I am starting up a company that will help make AI solutions sticky with companies but do it so that people are enabled and developing. I use Claude for a lot of stuff to help me scale. *I want my style sheets, doc and ppt/slide templates that fit the logo feel*. The templates should support content that range from simple messaging (bullets/boxes walking through a process simply) and detail (think brindlewick slides: multiple graphs, call out boxes for context bullets). I am both a google and msft user. I have a logo with color scheme. The template layouts should be contemporary (not futuristic) modern, accessible and clean (timeless). I want to be able to drop these templates and style sheet into any AI, MSoffice, or Google to be able to use it. I prefer light beige/white/eggshell background but I am also okay with a slide that has negative visual for impact.

```html
<!DOCTYPE html>
<html lang="en">
<head>
<meta charset="utf-8">
<title>Beacon &amp; Bloom Advisory — Slide Templates</title>
<link href="https://fonts.googleapis.com/css2?family=Poppins:wght@400;500;600;700&display=swap" rel="stylesheet">
<style>
:root{
  --navy:#1b2a4a;
  --teal:#136f77;
  --mint:#a6d9c8;
  --sage:#4da58a;
  --beige:#e8dfd2;
  --ink:#222a36;
  --paper:#fbfbfa;
  --stage:#cfcfcf;
  --muted:#5b6472;
}
*{box-sizing:border-box;margin:0;padding:0}
html,body{width:1001px;height:1200px;overflow:hidden}
body{background:var(--stage);font-family:'Poppins',sans-serif;color:var(--ink);position:relative}
.slide{position:absolute;width:426px;height:239px;background:var(--paper);overflow:hidden}
.slide>*{position:absolute}
.col-a{left:56px}.col-b{left:519px}
.row-1{top:61px}.row-2{top:339px}.row-3{top:619px}.row-4{top:899px}

.brand{display:flex;align-items:center;gap:4px;color:var(--navy);font-weight:500;white-space:nowrap;line-height:1.1}
.brand .dot{width:9px;height:9px;border-radius:50%;background:var(--teal);flex:none}
.brand-corner{right:22px;top:11px;font-size:7.5px}
.brand-corner .dot{width:7px;height:7px}

.title{left:22px;top:9px;font-size:13.5px;font-weight:600;color:var(--navy)}
.title em{font-style:normal;color:var(--teal)}
.title::before{content:"";position:absolute;left:0;top:-2px;width:22px;height:1.5px;background:var(--teal)}
.title::after{content:"";position:absolute;left:23px;top:-2px;width:12px;height:1.5px;background:var(--mint)}

.footer{left:0;bottom:0;width:426px;height:16.5px;font-size:5.8px;font-weight:500;color:#fff}
.footer svg{position:absolute;left:0;top:0}
.footer .copy{position:absolute;left:22px;top:4.5px}
.footer .page{position:absolute;right:22px;top:4.5px}

/* cover */
.cover-headline{left:21px;top:92px;font-size:14px;font-weight:700;color:var(--navy);line-height:1.25}
.cover-headline span{display:block;color:var(--teal);font-weight:500}
.cover-body{left:21px;top:132px;width:180px;font-size:8.6px;line-height:13.7px}
.cta{left:21px;top:181px;width:107px;height:19px;border-radius:10px;background:var(--sage);color:#fff;font-size:7.8px;font-weight:600;display:flex;align-items:center;justify-content:center}

/* agenda */
.agenda{left:22px;top:44px;list-style:none}
.agenda li{display:flex;align-items:center;gap:7px;height:24px;margin-bottom:15px;font-size:8.3px;font-weight:500;position:relative}
.agenda .num{width:24px;height:24px;border-radius:50%;background:var(--teal);color:#fff;display:flex;align-items:center;justify-content:center;font-size:11px;font-weight:600}
.agenda li:nth-child(odd) .num{background:var(--navy)}
.agenda li:not(:last-child)::after{content:"";position:absolute;left:11.5px;top:24px;height:15px;border-left:1px dotted var(--teal)}

.photo{background:linear-gradient(135deg,#8a7a6a,#3f3a36 60%,#1e2330)}

/* about */
.about-copy{left:22px;top:31px;width:176px;font-size:6px;line-height:9.7px}
.about-copy p{margin-bottom:9.7px}

/* services */
.card{top:59px;width:102px;height:125px;padding:26px 7px 0;text-align:center;color:#fff}
.card h3{font-size:6.8px;font-weight:600;line-height:10.5px;margin-bottom:6px}
.card p{font-size:5.6px;line-height:8.9px}
.card p+p{margin-top:8.9px}
.card .badge{position:absolute;left:34px;top:-19px;width:34px;height:34px;border-radius:50%;border:2px solid #fff;display:flex;align-items:center;justify-content:center}
.card-mint{left:24px;background:var(--mint)}
.card-mint .badge{background:var(--mint)}
.card-teal{left:154px;background:var(--teal)}
.card-teal .badge{background:var(--teal)}
.card-navy{left:284px;background:var(--navy)}
.card-navy .badge{background:var(--navy)}

/* section */
.section-brand{left:0;width:426px;top:108px;justify-content:center;font-size:17px}
.section-brand .dot{width:13px;height:13px}
.section-title{left:0;width:426px;top:143px;text-align:center;font-size:18px;font-weight:600;color:var(--navy)}
.section-rule{left:198px;top:168px;width:30px;height:1.5px;background:var(--teal)}

/* process */
.step{width:112px;font-size:5.7px;line-height:9.7px;color:var(--ink)}
.step h4{font-size:6.5px;font-weight:600;margin-bottom:3px}
.step-left{text-align:right}
.ring{width:32px;height:32px;border-radius:50%;border:1.5px solid #fff;box-shadow:0 0 0 1.3px var(--teal);display:flex;align-items:center;justify-content:center}
.ring-mint{background:var(--mint)}.ring-teal{background:var(--teal)}.ring-navy{background:var(--navy);box-shadow:0 0 0 1.3px var(--navy)}
.process-brand{left:146px;top:109px;width:134px;justify-content:center;font-size:13px;white-space:normal;text-align:center}

/* graph */
.chart-head{top:41px;width:186px;height:17px;color:#fff;font-size:7px;font-weight:500;display:flex;align-items:center;justify-content:center}

/* contact */
.contact-brand{left:20px;top:118px;width:192px;justify-content:center;font-size:17px;white-space:normal;text-align:center}
.contact-rule{left:229px;top:41px;width:1px;height:134px;background:var(--teal)}
.contact-title{left:251px;top:46px;font-size:13px;font-weight:600;color:var(--navy)}
.contact-title em{font-style:normal;color:var(--teal)}
.contact-list{left:251px;top:74px;list-style:none}
.contact-list li{display:flex;gap:8px;margin-bottom:9px;font-size:6.8px;line-height:10.5px}
.contact-list b{font-weight:600;display:block}
.contact-list .ico{width:16px;height:16px;border-radius:50%;background:var(--teal);flex:none;margin-top:2px;display:flex;align-items:center;justify-content:center}
</style>
</head>
<body>

<svg width="0" height="0" style="position:absolute">
  <defs>
    <g id="footer-bands">
      <polygon points="0,0 292,0 298,16.5 0,16.5" fill="#1b2a4a"/>
      <polygon points="296,0 426,0 426,16.5 302,16.5" fill="#136f77"/>
    </g>
  </defs>
</svg>

<!-- Cover -->
<section class="slide col-a row-1">
  <svg width="426" height="239" style="left:0;top:0">
    <polygon points="236,239 426,52 426,239" fill="#1b2a4a"/>
    <rect x="360" y="10" width="14" height="60" rx="7" fill="#1b2a4a" transform="rotate(45 367 40)"/>
    <rect x="398" y="18" width="16" height="70" rx="8" fill="#a6d9c8" transform="rotate(45 406 53)"/>
    <rect x="216" y="150" width="16" height="68" rx="8" fill="#136f77" transform="rotate(45 224 184)"/>
    <rect x="252" y="178" width="16" height="60" rx="8" fill="#4da58a" transform="rotate(45 260 208)"/>
    <circle cx="321" cy="128" r="83" fill="#fff" stroke="#136f77" stroke-width="1"/>
  </svg>
  <div role="img" aria-label="Glowing blue AI interface illustration with a hand touching a central AI button" style="left:247px;top:54px;width:148px;height:148px;border-radius:50%;background:radial-gradient(circle,#5a3fd8 0%,#2331a8 45%,#101a4e 100%)"></div>
  <div class="brand" style="left:21px;top:62px;font-size:12px"><span class="dot"></span>Beacon &amp; Bloom Advisory</div>
  <h1 class="cover-headline">Making AI Work for People,<span>Not Just Systems</span></h1>
  <p class="cover-body">We help organizations adopt AI in ways that stick—by developing people, not just deploying tools.</p>
  <div class="cta">Start a Conversation</div>
</section>

<!-- Agenda -->
<section class="slide col-b row-1">
  <h2 class="title">Agenda</h2>
  <div class="brand brand-corner"><span class="dot"></span>Beacon &amp; Bloom Advisory</div>
  <ol class="agenda">
    <li><span class="num">1</span>Executive Summary</li>
    <li><span class="num">2</span>Company Overview</li>
    <li><span class="num">3</span>Platform for Unparalleled Growth</li>
    <li><span class="num">4</span>Premium Financial Results</li>
  </ol>
  <svg width="426" height="239" style="left:0;top:0">
    <polyline points="312,48 399,48 399,123" fill="none" stroke="#1b2a4a" stroke-width="2"/>
    <polyline points="228,121 228,196 315,196" fill="none" stroke="#136f77" stroke-width="2"/>
  </svg>
  <div class="photo" role="img" aria-label="Photo of a small robot writing with a pencil at a desk" style="left:234px;top:51px;width:161px;height:141px"></div>
  <div class="footer"><svg width="426" height="16.5"><use href="#footer-bands"/></svg><span class="copy">© 2026 Beacon &amp; Bloom Advisory, LLC. All rights reserved.</span><span class="page">Page Number: 02</span></div>
</section>

<!-- About -->
<section class="slide col-a row-2">
  <h2 class="title">About <em>Us</em></h2>
  <div class="brand brand-corner"><span class="dot"></span>Beacon &amp; Bloom Advisory</div>
  <div class="about-copy">
    <p>Beacon &amp; Bloom Advisory partners with founders, C-suite executives, and investors to unlock revenue potential and operational excellence.</p>
    <p>We operated in the seat. We know what breaks. We specialize in diagnosing the hidden friction points that slow growth, creating the operational clarity needed for scaling, and implementing AI solutions that your teams will actually want to use.</p>
    <p>Our approach combines strategic insight with practical execution, ensuring sustainable growth and competitive advantage</p>
    <p>Beacon &amp; Bloom Advisory partners with founders, C-suite executives, and investors to unlock revenue potential and operational excellence.</p>
  </div>
  <svg width="426" height="239" style="left:0;top:0">
    <circle cx="321" cy="124" r="82" fill="none" stroke="#136f77" stroke-width="0.8"/>
    <circle cx="321" cy="124" r="78" fill="none" stroke="#136f77" stroke-width="0.8"/>
  </svg>
  <div class="photo" role="img" aria-label="Photo of two colleagues reviewing a laptop in a server room" style="left:247px;top:50px;width:148px;height:148px;border-radius:50%;background:linear-gradient(160deg,#2b3f5e,#0f1a33 70%,#1f4c7a)"></div>
  <div class="footer"><svg width="426" height="16.5"><use href="#footer-bands"/></svg><span class="copy">© 2026 Beacon &amp; Bloom Advisory, LLC. All rights reserved.</span><span class="page">Page Number: 03</span></div>
</section>

<!-- Services -->
<section class="slide col-b row-2">
  <h2 class="title">Our <em>Services</em></h2>
  <div class="brand brand-corner"><span class="dot"></span>Beacon &amp; Bloom Advisory</div>
  <article class="card card-mint">
    <span class="badge"><svg width="14" height="14" viewBox="0 0 14 14" fill="none" stroke="#fff" stroke-width="1.2"><rect x="2" y="2" width="10" height="7"/><path d="M7 9v3M4 12h6M4 7l2-2 2 1 2-3"/></svg></span>
    <h3>GTM Strategy &amp; Revenue Optimization</h3>
    <p>Diagnose revenue friction and design go-to-market strategies that accelerate growth.</p>
    <p>We help you identify market opportunities, refine your positioning.</p>
  </article>
  <article class="card card-teal">
    <span class="badge"><svg width="14" height="14" viewBox="0 0 14 14" fill="none" stroke="#fff" stroke-width="1.2"><circle cx="7" cy="5" r="3"/><circle cx="7" cy="5" r="1"/><path d="M2 13v-2a2 2 0 0 1 4 0v2M8 13v-2a2 2 0 0 1 4 0v2"/></svg></span>
    <h3>RevOps &amp; Operational Clarity</h3>
    <p>Build the operational infrastructure your business needs to scale. We streamline processes, align teams, and create the systems and clarity that enable efficient growth and better decision-making.</p>
  </article>
  <article class="card card-navy">
    <span class="badge"><svg width="14" height="14" viewBox="0 0 14 14" fill="none" stroke="#fff" stroke-width="1.2"><circle cx="7" cy="7" r="3.5"/><path d="M7 1v2M7 11v2M1 7h2M11 7h2M3 3l1.4 1.4M9.6 9.6 11 11M11 3 9.6 4.4M4.4 9.6 3 11"/></svg></span>
    <h3>AI Adoption &amp; Implementation</h3>
    <p>Deploy outcomes-based AI solutions that your teams embrace rather than tolerate. We guide you through thoughtful AI use cases and solution development that incorporate change management.</p>
  </article>
  <div class="footer"><svg width="426" height="16.5"><use href="#footer-bands"/></svg><span class="copy">© 2026 Beacon &amp; Bloom Advisory, LLC. All rights reserved.</span><span class="page">Page Number: 04</span></div>
</section>

<!-- Section divider -->
<section class="slide col-a row-3">
  <div class="brand section-brand"><span class="dot"></span>Beacon &amp; Bloom Advisory</div>
  <h2 class="section-title">Introductions</h2>
  <span class="section-rule"></span>
  <div class="footer"><svg width="426" height="16.5"><use href="#footer-bands"/></svg><span class="copy">© 2026 Beacon &amp; Bloom Advisory, LLC. All rights reserved.</span><span class="page">Page Number: 05</span></div>
</section>

<!-- Process -->
<section class="slide col-b row-3">
  <h2 class="title">How <em>You</em> Work</h2>
  <div class="brand brand-corner"><span class="dot"></span>Beacon &amp; Bloom Advisory</div>
  <div class="brand process-brand">Beacon &amp; Bloom Advisory</div>
  <div class="step step-left" style="left:9px;top:67px"><h4>Discover</h4>We prioritize a smaller portfolio to maximize returns for each Investment.</div>
  <div class="step step-left" style="left:9px;top:129px"><h4>Develop</h4>Our approach is centered on addressing challenges and/or supporting milestones to unlock each company’s full potential</div>
  <div class="step" style="left:304px;top:60px"><h4>Design</h4>Employs internal due diligence and document review procedures to ensure cost-effective and timely execution of opportunities.</div>
  <div class="step" style="left:304px;top:129px"><h4>Deploy</h4>We leverage our established network of professionals and investment partners to explore new opportunities.</div>
  <span class="ring ring-mint" style="left:128px;top:68px"><svg width="14" height="14" viewBox="0 0 14 14" fill="none" stroke="#fff" stroke-width="1.2"><circle cx="7" cy="7" r="5"/><circle cx="7" cy="7" r="2"/></svg></span>
  <span class="ring ring-teal" style="left:128px;top:131px"><svg width="14" height="14" viewBox="0 0 14 14" fill="none" stroke="#fff" stroke-width="1.2"><circle cx="7" cy="4" r="2"/><path d="M3 12v-2a4 4 0 0 1 8 0v2"/></svg></span>
  <span class="ring ring-teal" style="left:264px;top:68px"><svg width="14" height="14" viewBox="0 0 14 14" fill="none" stroke="#fff" stroke-width="1.2"><path d="M11 5a4.5 4.5 0 0 0-8 0M3 9a4.5 4.5 0 0 0 8 0M11 2v3H8M3 12V9h3"/></svg></span>
  <span class="ring ring-navy" style="left:264px;top:131px"><svg width="14" height="14" viewBox="0 0 14 14" fill="none" stroke="#fff" stroke-width="1.2"><path d="M4 10a3 3 0 0 1 0-6 4 4 0 0 1 7 1 2.5 2.5 0 0 1 0 5z"/></svg></span>
  <div class="footer"><svg width="426" height="16.5"><use href="#footer-bands"/></svg><span class="copy">© 2026 Beacon &amp; Bloom Advisory, LLC. All rights reserved.</span><span class="page">Page Number: 06</span></div>
</section>

<!-- Graphs -->
<section class="slide col-a row-4">
  <h2 class="title">Our Graph</h2>
  <div class="brand brand-corner"><span class="dot"></span>Beacon &amp; Bloom Advisory</div>
  <div class="chart-head" style="left:22px;background:var(--teal)">Historical and Projected PF Revenue</div>
  <div class="chart-head" style="left:219px;background:var(--navy)">Historical and Projected PF Revenue</div>
  <svg width="426" height="239" style="left:0;top:0" font-family="Poppins, sans-serif">
    <text x="115" y="72" font-size="5.6" fill="#a6d9c8" text-anchor="middle">Historical and Projected PF Revenue</text>
    <g font-size="3.4" fill="#444" text-anchor="end">
      <text x="38" y="81">120</text><text x="38" y="97">100</text><text x="38" y="114">80</text><text x="38" y="130">60</text><text x="38" y="146">40</text><text x="38" y="162">20</text><text x="38" y="178">0</text>
    </g>
    <rect x="42" y="79" width="153" height="97" fill="none" stroke="#ddd" stroke-width="0.5"/>
    <g fill="#136f77">
      <rect x="48" y="96" width="4" height="80"/><rect x="70" y="104" width="4" height="72"/><rect x="92" y="136" width="4" height="40"/><rect x="114" y="96" width="4" height="80"/><rect x="136" y="96" width="4" height="80"/><rect x="158" y="128" width="4" height="48"/><rect x="180" y="136" width="4" height="40"/>
    </g>
    <g fill="#a6d9c8">
      <rect x="54" y="104" width="4" height="72"/><rect x="76" y="112" width="4" height="64"/><rect x="98" y="96" width="4" height="80"/><rect x="120" y="128" width="4" height="48"/><rect x="142" y="104" width="4" height="72"/><rect x="164" y="116" width="4" height="60"/><rect x="186" y="96" width="4" height="80"/>
    </g>
    <g font-size="3.2" fill="#222" text-anchor="middle">
      <text x="50" y="94">100</text><text x="56" y="102">90</text><text x="72" y="102">90</text><text x="78" y="110">80</text><text x="94" y="134">50</text><text x="100" y="94">100</text><text x="116" y="94">100</text><text x="122" y="126">60</text><text x="138" y="94">100</text><text x="144" y="102">90</text><text x="160" y="126">60</text><text x="166" y="114">75</text><text x="182" y="134">50</text><text x="188" y="94">100</text>
    </g>
    <g font-size="3.6" fill="#222" text-anchor="middle">
      <text x="53" y="182">Jan</text><text x="75" y="182">Feb</text><text x="97" y="182">Mar</text><text x="119" y="182">Apr</text><text x="141" y="182">May</text><text x="163" y="182">Jun</text><text x="185" y="182">Jul</text>
    </g>
    <text x="122" y="194" font-size="5" fill="#222" text-anchor="middle">CAGR 43%</text>

    <text x="311" y="74" font-size="5" fill="#1b2a4a" text-anchor="middle">Historical and Projected PF EBITDA</text>
    <g font-size="3" fill="#777" text-anchor="end">
      <text x="238" y="90">25k</text><text x="238" y="101">20k</text><text x="238" y="112">15k</text><text x="238" y="122">10k</text><text x="238" y="133">5k</text>
    </g>
    <text x="223" y="115" font-size="3" fill="#777" transform="rotate(-90 223 115)" text-anchor="middle">Reviews</text>
    <g fill="#e8dfd2">
      <rect x="248" y="115" width="9" height="22"/><rect x="261" y="102" width="9" height="35"/><rect x="274" y="115" width="9" height="22"/><rect x="300" y="120" width="9" height="17"/><rect x="313" y="105" width="9" height="32"/><rect x="326" y="109" width="9" height="28"/><rect x="339" y="116" width="9" height="21"/><rect x="352" y="102" width="9" height="35"/><rect x="365" y="109" width="9" height="28"/><rect x="378" y="102" width="9" height="35"/><rect x="391" y="109" width="9" height="28"/>
    </g>
    <rect x="287" y="93" width="9" height="44" rx="1.5" fill="#1b2a4a"/>
    <g font-size="3" fill="#777" text-anchor="middle">
      <text x="252" y="150">Jan</text><text x="265" y="150">Feb</text><text x="278" y="150">Mar</text><text x="291" y="150">Apr</text><text x="304" y="150">May</text><text x="317" y="150">Jun</text><text x="330" y="150">Jul</text><text x="343" y="150">Aug</text><text x="356" y="150">Sep</text><text x="369" y="150">Oct</text><text x="382" y="150">Nov</text><text x="395" y="150">Dec</text>
      <text x="312" y="161">year</text>
    </g>
    <text x="311" y="179" font-size="5" fill="#1b2a4a" text-anchor="middle">EBITDA EBITDA Margin</text>
  </svg>
  <div class="footer"><svg width="426" height="16.5"><use href="#footer-bands"/></svg><span class="copy">© 2026 Beacon &amp; Bloom Advisory, LLC. All rights reserved.</span><span class="page">Page Number: 07</span></div>
</section>

<!-- Contact -->
<section class="slide col-b row-4">
  <div class="brand contact-brand"><span class="dot"></span>Beacon &amp; Bloom Advisory</div>
  <span class="contact-rule"></span>
  <h2 class="contact-title">Contact <em>Us</em></h2>
  <ul class="contact-list">
    <li><span class="ico"><svg width="8" height="8" viewBox="0 0 10 10" fill="#fff"><path d="M2 1l2 2-1 1.3a6 6 0 0 0 2.7 2.7L7 6l2 2-1.3 1.3C4.5 9 1 5.5.7 2.3z"/></svg></span><div><b>Phone:</b>+1 555 010 2040</div></li>
    <li><span class="ico"><svg width="8" height="8" viewBox="0 0 10 10" fill="#fff"><path d="M1 2h8v6H1z"/><path d="M1 2l4 3 4-3" stroke="#136f77" fill="none" stroke-width="0.8"/></svg></span><div><b>Email:</b>info@beaconbloomadvisory.com</div></li>
    <li><span class="ico"><svg width="8" height="8" viewBox="0 0 10 10" fill="#fff"><path d="M5 0.5a3.2 3.2 0 0 1 3.2 3.2C8.2 6 5 9.5 5 9.5S1.8 6 1.8 3.7A3.2 3.2 0 0 1 5 .5z"/><circle cx="5" cy="3.7" r="1.1" fill="#136f77"/></svg></span><div><b>Location:</b>Beacon &amp; Bloom Advisory,<br>United State.</div></li>
  </ul>
  <div class="footer"><svg width="426" height="16.5"><use href="#footer-bands"/></svg><span class="copy">© 2026 Beacon &amp; Bloom Advisory, LLC. All rights reserved.</span><span class="page">Page Number: 08</span></div>
</section>

</body>
</html>
```